Help a start up law firm make an impression! - Website

We are a property development and conveyancing law firm looking for some to design our website. The initial brief is for 6 pages with scope for on-going work.

Law firms are traditionally quite conservative and we want to break the mold. We want to come across as fun and modern, while still being professional.

A good example is https://quorrantlaw.com.au/. It's professional yet modern.
Updates

Another good site I like in the same industry: https://www.tindalemarshconveyancing.com.au/

Target Market(s)

Tech savy home buyers and sellers - generally 30 to 50 years old

Industry/Entity Type

Law Firm

Coding

Coded - Design and coding required

Number of Pages Required

5+ page

Font styles to use
Other font styles liked:
• No idea

Colors
f04a50

Requirements
Must have
• The elements set out in the design brief document

```html
<!DOCTYPE html>
<html lang="en">
<head>
<meta charset="utf-8">
<title>Marrick Law — The Property Law Experts</title>
<link href="https://fonts.googleapis.com/css2?family=Source+Sans+3:ital,wght@0,300;0,400;0,600;0,700;1,400&display=swap" rel="stylesheet">
<style>
:root{
  --brand:#c4435a;
  --brand-deep:#5c0d1d;
  --brand-soft:#ecc4cc;
  --brand-tint:#f7d9df;
  --ink:#2a2a2a;
  --muted:#4a4a4a;
  --white:#ffffff;
  --dark:#161616;
}
*{box-sizing:border-box;margin:0;padding:0}
html,body{width:1200px;height:3482px;overflow:hidden}
body{font-family:"Source Sans 3",Arial,sans-serif;color:var(--ink);background:var(--white);position:relative}
a{color:inherit;text-decoration:none}

.site-header{position:absolute;top:0;left:0;width:1200px;height:93px;background:var(--brand);color:var(--white)}
.brand-name{position:absolute;left:24px;top:20px;font-size:50px;font-weight:700;letter-spacing:-0.5px;color:var(--white)}
.call{position:absolute;right:30px;top:8px;display:flex;align-items:center;gap:12px;font-size:16px}
.call-number{border:2px solid var(--white);padding:2px 12px;font-size:30px;font-weight:400;line-height:34px}
.main-nav{position:absolute;right:30px;top:58px;display:flex;gap:22px;font-size:16px}
.main-nav a{position:relative;padding-left:14px}
.main-nav a::before{content:"";position:absolute;left:0;top:8px;width:7px;height:7px;border-radius:50%;background:var(--white)}
.main-nav a.current{padding-left:0;border-bottom:2px solid var(--white)}
.main-nav a.current::before{display:none}

.hero{position:absolute;top:93px;left:0;width:1200px;height:629px;background:linear-gradient(100deg,#e6b9c3 0%,#f0cbd2 35%,#d9a0ad 60%,#c88391 100%);text-align:center;color:var(--white)}
.hero-title{position:absolute;top:335px;width:100%;font-size:46px;font-weight:400;letter-spacing:0.5px}
.hero-sub{position:absolute;top:400px;left:50%;transform:translateX(-50%);width:560px;font-size:26px;line-height:34px;font-weight:400}
.btn-solid{display:inline-block;background:var(--brand);color:var(--white);font-size:20px;padding:8px 26px}
.hero .btn-solid{position:absolute;top:492px;left:50%;transform:translateX(-50%)}
.slider-dots{position:absolute;top:592px;left:50%;transform:translateX(-50%);display:flex;gap:8px}
.slider-dots span{width:9px;height:9px;border-radius:50%;background:rgba(255,255,255,.6)}
.slider-dots span.on{background:var(--white)}

.features{position:absolute;top:722px;left:0;width:1200px;height:415px}
.feature{position:absolute;top:68px;width:290px;text-align:center}
.feature-icon{width:92px;height:92px;border-radius:50%;background:var(--brand);margin:0 auto;display:flex;align-items:center;justify-content:center}
.feature h3{margin-top:20px;font-size:32px;font-weight:400;color:var(--brand)}
.feature p{margin-top:10px;font-size:16px;line-height:20px;color:var(--ink);padding:0 6px}
.read-more{display:block;margin-top:18px;font-size:15px;color:var(--brand)}

.about{position:absolute;top:1137px;left:0;width:1200px;height:727px;background:radial-gradient(ellipse at 50% 60%,#3a3a3a 0%,#1d1d1d 55%,#0e0e0e 100%);color:var(--white);text-align:center}
.about-icon{position:absolute;top:14px;left:50%;transform:translateX(-50%)}
.box-heading{display:inline-block;border:2px solid var(--white);font-weight:400;color:var(--white)}
.about > .box-heading{position:absolute;top:42px;left:480px;width:242px;height:65px;line-height:61px;font-size:22px}
.about-intro{position:absolute;top:160px;left:150px;width:900px;font-size:14px;line-height:18px;font-style:italic}
.about-card{position:absolute;top:330px;width:326px;height:325px;background:rgba(120,120,120,.55);padding:0 22px}
.about-card .box-heading{margin-top:32px;font-size:18px;padding:10px 32px;border-width:1px}
.about-card p{margin-top:18px;font-size:15px;line-height:19px}
.about-card .btn-solid{margin-top:18px;font-size:15px;padding:5px 16px;border:1px solid #e88;}
.card-icon{position:absolute;top:10px;left:50%;transform:translateX(-50%)}

.knowledge{position:absolute;top:1864px;left:0;width:1200px;height:608px;text-align:center}
.section-title{position:absolute;top:68px;width:100%;font-size:25px;font-weight:400;color:var(--brand)}
.post{position:absolute;top:185px;width:348px}
.post-frame{height:233px;border:1px solid #d8d8d8;background:linear-gradient(var(--brand-tint) 0,var(--brand-tint) 58px,var(--white) 58px);padding:18px 24px 0}
.post-photo{height:187px}
.post h4{margin-top:28px;font-size:20px;font-weight:400;color:var(--brand)}
.post p{margin-top:6px;font-size:15px;line-height:19px;padding:0 30px}

.contact{position:absolute;top:2472px;left:0;width:1200px;height:638px;background:var(--brand);color:var(--white);text-align:center}
.contact-icon{position:absolute;top:18px;left:50%;transform:translateX(-50%)}
.contact .box-heading{position:absolute;top:46px;left:478px;width:244px;height:63px;line-height:59px;font-size:32px}
.contact-lead{position:absolute;top:126px;width:100%;font-size:20px}
.contact-form .field{position:absolute;background:var(--white);border-radius:4px;color:var(--muted);font-size:15px;text-align:left;padding:12px 24px}
.contact-form .submit{position:absolute;left:283px;top:548px;width:638px;height:46px;background:var(--brand-deep);color:var(--white);font-size:20px;font-weight:700;line-height:46px;border-radius:4px}

.site-footer{position:absolute;top:3110px;left:0;width:1200px;height:283px;background:var(--brand-soft);text-align:center}
.footer-brand{position:absolute;top:64px;width:100%;font-size:34px;font-weight:700;color:var(--brand)}
.footer-nav{position:absolute;top:146px;width:100%;display:flex;justify-content:center;gap:26px;font-size:15px;color:var(--ink)}
.social{position:absolute;top:198px;left:50%;transform:translateX(-50%);display:flex;gap:22px}
.social span{width:36px;height:36px;border-radius:50%;border:2px solid var(--brand)}
.copyright{position:absolute;top:3393px;left:0;width:1200px;height:89px;background:var(--brand);color:var(--white);font-size:15px;line-height:89px;text-align:center}
</style>
</head>
<body>

<header class="site-header">
  <div class="brand-name">Marrick Law</div>
  <div class="call"><span>CALL</span><span class="call-number">1.800.555.0142</span></div>
  <nav class="main-nav">
    <a class="current" href="#">Home</a>
    <a href="#">Conveyancing</a>
    <a href="#">Property Development</a>
    <a href="#">News &amp; Knowledge</a>
    <a href="#">About Us</a>
  </nav>
</header>

<section class="hero" role="img" aria-label="Two smiling clients talking across a table in a bright office, tinted pink">
  <h1 class="hero-title">THE PROPERTY LAW EXPERTS</h1>
  <p class="hero-sub">Unrivaled response times, fixed fee options and experienced property lawyers</p>
  <a class="btn-solid" href="#">GET IN TOUCH</a>
  <div class="slider-dots"><span class="on"></span><span></span><span></span><span></span></div>
</section>

<section class="features">
  <div class="feature" style="left:0">
    <div class="feature-icon"><svg width="50" height="50" viewBox="0 0 50 50" fill="none" stroke="#fff" stroke-width="2.5"><rect x="6" y="8" width="20" height="6"/><rect x="6" y="16" width="20" height="6"/><rect x="6" y="24" width="20" height="6"/><rect x="6" y="32" width="20" height="6"/><circle cx="34" cy="32" r="11"/><path d="M34 25v14M37 28h-4a2 2 0 000 4h2a2 2 0 010 4h-4"/></svg></div>
    <h3>Cost Certainty</h3>
    <p>Flexible fee arrangements with no surprises. We offer fixed fee, pay on completion and monthly retainer options to suit your needs.</p>
    <a class="read-more" href="#">Read More &gt;</a>
  </div>
  <div class="feature" style="left:305px">
    <div class="feature-icon"><svg width="50" height="50" viewBox="0 0 50 50" fill="none" stroke="#fff" stroke-width="2.5"><circle cx="25" cy="18" r="8"/><path d="M11 42c2-9 8-13 14-13s12 4 14 13"/><path d="M22 30l3 6 3-6"/></svg></div>
    <h3>Expert Lawyers</h3>
    <p>Our experienced team has managed over 2,000 conveyances and worked on some of the most iconic developments</p>
    <a class="read-more" href="#">Read More &gt;</a>
  </div>
  <div class="feature" style="left:607px">
    <div class="feature-icon"><svg width="50" height="50" viewBox="0 0 50 50" fill="none" stroke="#fff" stroke-width="2.5"><circle cx="25" cy="25" r="19"/><path d="M17 15c-2 2-2 6 2 11s9 9 13 9c2 0 3-2 3-3l-4-4-3 2c-2-1-5-4-6-6l2-3-4-4z"/></svg></div>
    <h3>Responsive Service</h3>
    <p>The most responsive service, guaranteed. No more waiting days for a lawyer to respond to your email, return your call or prepare.</p>
    <a class="read-more" href="#">Read More &gt;</a>
  </div>
  <div class="feature" style="left:904px">
    <div class="feature-icon"><svg width="50" height="50" viewBox="0 0 50 50" fill="none" stroke="#fff" stroke-width="2.5"><path d="M8 42V18l17-9 17 9v24z"/><rect x="16" y="24" width="18" height="18"/><path d="M16 30h18M16 36h18"/></svg></div>
    <h3>Commercial Advice</h3>
    <p>We work with you to get the deal done without legal jargon getting in the way. We understand timing is crucial and we focus on the legal .</p>
    <a class="read-more" href="#">Read More &gt;</a>
  </div>
</section>

<section class="about">
  <svg class="about-icon" width="48" height="48" viewBox="0 0 48 48" fill="#fff"><rect x="18" y="4" width="14" height="22" rx="2" transform="rotate(45 25 15)"/><rect x="6" y="26" width="6" height="22" rx="2" transform="rotate(-45 9 37)"/></svg>
  <h2 class="box-heading">ABOUT US</h2>
  <p class="about-intro">Lorem Ipsum is simply dummy text of the printing and typesetting industry. Lorem Ipsum has been the industry's standard dummy text ever since the 1500s, when an unknown printer took a galley of type and scrambled it to make a type specimen book. It has survived not only five centuries, but also the leap into electronic typesetting, remaining essentially unchanged.</p>

  <div class="about-card" style="left:26px">
    <h3 class="box-heading">WHO WE ARE</h3>
    <p>Marrick Law is a specialised property development law firm established to assist small to medium property developers with their Queensland developments. We offer a comprehensive service from site acquisition through to conveyancing of finished stock.</p>
    <a class="btn-solid" href="#">Read More &gt;</a>
  </div>
  <div class="about-card" style="left:434px">
    <svg class="card-icon" width="32" height="32" viewBox="0 0 32 32" fill="none" stroke="#fff" stroke-width="2"><circle cx="16" cy="15" r="12"/><path d="M12 12a4 4 0 118 0c0 3-4 3-4 6M16 22v1"/></svg>
    <h3 class="box-heading">WHAT WE DO</h3>
    <p>Looking for off the plan contracts, joint venture agreements, management rights sale agreements, caretaking agreements, letting agreements and more? If it's related to property development, Marrick Law can help.</p>
    <a class="btn-solid" href="#">Read More &gt;</a>
  </div>
  <div class="about-card" style="left:850px">
    <h3 class="box-heading">WHERE WE WORK</h3>
    <p>Marrick Law is a specialised property development law firm established to assist small to medium property developers with their Queensland developments. We offer a comprehensive service from site acquisition through to conveyancing of finished stock.</p>
    <a class="btn-solid" href="#">Read More &gt;</a>
  </div>
</section>

<section class="knowledge">
  <h2 class="section-title">KNOWLEDGE AND NEWS</h2>
  <article class="post" style="left:30px">
    <div class="post-frame"><div class="post-photo" role="img" aria-label="Looking up at city office towers" style="background:linear-gradient(160deg,#9fb4c6,#3e5a74 55%,#1f3348)"></div></div>
    <h4>Blog Post Title</h4>
    <p>Lorem Ipsum is simply dummy text of the printing and typesetting industry. Lorem Ipsum has been the industry's standard dummy text ever since the 1500s</p>
  </article>
  <article class="post" style="left:429px">
    <div class="post-frame"><div class="post-photo" role="img" aria-label="Silhouetted business people beside tall windows" style="background:linear-gradient(180deg,#d7eaf7,#5f9bd0 50%,#123f73)"></div></div>
    <h4>Real estate laws on the move</h4>
    <p>Lorem Ipsum is simply dummy text of the printing and typesetting industry. Lorem Ipsum has been the industry's standard dummy text ever since the 1500s</p>
  </article>
  <article class="post" style="left:829px">
    <div class="post-frame"><div class="post-photo" role="img" aria-label="Two businessmen in suits talking in a bright lobby" style="background:linear-gradient(180deg,#eef2f6,#c7d3df 60%,#7c8a99)"></div></div>
    <h4>Private equity firm takes control</h4>
    <p>Lorem Ipsum is simply dummy text of the printing and typesetting industry. Lorem Ipsum has been the industry's standard dummy text ever since the 1500s</p>
  </article>
</section>

<section class="contact">
  <svg class="contact-icon" width="40" height="30" viewBox="0 0 40 30" fill="none" stroke="#fff" stroke-width="2.5"><path d="M6 18c0-8 6-14 14-14s14 6 14 14"/><rect x="2" y="16" width="8" height="11" rx="3" fill="#fff"/><rect x="30" y="16" width="8" height="11" rx="3" fill="#fff"/></svg>
  <h2 class="box-heading">Contact Us</h2>
  <p class="contact-lead">Fill out the form below to get in touch.</p>
  <form class="contact-form">
    <div class="field" style="left:283px;top:174px;width:307px;height:46px">First Name</div>
    <div class="field" style="left:615px;top:174px;width:306px;height:46px">Last Name</div>
    <div class="field" style="left:283px;top:239px;width:307px;height:46px">Email Address</div>
    <div class="field" style="left:615px;top:239px;width:306px;height:46px">Phone Number</div>
    <div class="field" style="left:283px;top:304px;width:638px;height:227px">Message</div>
    <div class="submit">SUBMIT</div>
  </form>
</section>

<footer class="site-footer">
  <div class="footer-brand">Marrick Law</div>
  <nav class="footer-nav">
    <a href="#">HOME</a><a href="#">CONVEYANCING</a><a href="#">PROPERTY DEVELOPMENT</a><a href="#">NEWS &amp; KNOWLEDGE</a><a href="#">ABOUT US</a>
  </nav>
  <div class="social"><span></span><span></span><span></span></div>
</footer>
<div class="copyright">COPYRIGHT 2017 MARRICK LAW</div>

</body>
</html>
```